Verlane Area Planning Council Business Cards

We're looking for a business card design, simple as that. We're a local government agency that mainly performs building code enforcement, transportation planning, floodplain management, and GIS for Tobinet Parish in Louisiana, and other surround parishes. So you're not having to Google anything, GIS is, at it's core, mapping. Building Code Enforcement is just that, nothing more. Floodplain Management is to make sure the public is within what the government

Contact Information for Business Card

Our Address is

417 Merriwell Avenue
Harlow Falls, ST 70000

Our phone is 5550192734
Our fax is 5550192739
Our website is www.vlpk.example
My email is dana@vlpk.example

Font styles to use
Serif
Sans Serif

Colors

Designer to choose colors to be used in the design.

Requirements
Must have
• I'm attaching our logo(several versions) that must be incorporated. The design should fit well with our existing logo. I can send photoshop files for our logo if needed. If possible, I'd like to be able to add names/info to each card for all of our employees once this is done.
Nice to have
• The regional emblem is a bonus, and isn't specifically required.

```html
<!DOCTYPE html>
<html lang="en">
<head>
<meta charset="utf-8">
<title>Verlane Area Planning Council Business Cards</title>
<link rel="stylesheet" href="https://fonts.googleapis.com/css2?family=Montserrat:wght@700&family=Open+Sans:wght@400;600&display=swap">
<style>
  :root {
    --backdrop: #e7e5e2;
    --card-dark: #2f2f31;
    --card-light: #ffffff;
    --text-light: #e6e6e6;
    --text-muted: #bdbdbd;
    --icon-blue: #2f6fb3;
    --emblem-line: rgba(255, 255, 255, 0.08);
  }
  * { box-sizing: border-box; margin: 0; padding: 0; }
  html, body { width: 1200px; height: 800px; overflow: hidden; }
  body {
    background: var(--backdrop);
    font-family: "Open Sans", Arial, sans-serif;
    position: relative;
  }
  .card {
    position: absolute;
    left: 320px;
    width: 560px;
    height: 320px;
    overflow: hidden;
    border-radius: 4px;
    box-shadow: 0 6px 18px rgba(0,0,0,0.18);
    background: var(--card-dark);
  }
  .card-front { top: 50px; }
  .card-back { top: 430px; }

  .front-band {
    position: absolute; left: 0; top: 0;
    width: 100%; height: 118px;
    background: var(--card-light);
  }
  .brand {
    position: absolute;
    display: flex; align-items: center; gap: 10px;
    font-family: "Montserrat", Arial, sans-serif;
    font-weight: 700;
    white-space: nowrap;
  }
  .brand-mark { width: 22px; height: 22px; border-radius: 50%; flex: none; }
  .card-front .brand { left: 34px; top: 74px; color: var(--card-dark); font-size: 19px; }
  .card-front .brand-mark { background: var(--card-dark); }
  .card-back .brand {
    left: 50%; top: 50%; transform: translate(-50%, -50%);
    color: var(--card-light); font-size: 24px;
  }
  .card-back .brand-mark { background: var(--card-light); width: 26px; height: 26px; }

  .emblem { position: absolute; border-radius: 50%; }
  .card-front .emblem {
    right: 50px; top: 136px; width: 110px; height: 110px;
    border: 2px solid var(--emblem-line);
    background: radial-gradient(circle, rgba(255,255,255,0.05), rgba(255,255,255,0.02));
  }
  .card-back .emblem {
    left: 50%; top: 50%; width: 260px; height: 260px;
    transform: translate(-50%, -50%);
    border: 3px solid var(--emblem-line);
    background: radial-gradient(circle, rgba(255,255,255,0.04), rgba(255,255,255,0.01));
  }

  .contact-rule {
    position: absolute; left: 34px; top: 128px;
    width: 210px; height: 1px; background: var(--text-light);
  }
  .contact {
    position: absolute; left: 34px; top: 138px;
    color: var(--text-light); font-size: 11.5px; line-height: 1.55;
  }
  .contact-name {
    font-weight: 600; font-size: 13px; text-decoration: underline;
    text-underline-offset: 3px; margin-bottom: 6px;
  }
  .contact-address { color: var(--text-muted); margin-bottom: 4px; }
  .contact-list { list-style: none; }
  .contact-list li { display: flex; align-items: center; gap: 8px; color: var(--text-muted); }
  .contact-icon { width: 12px; height: 12px; flex: none; }
</style>
</head>
<body>
  <section class="card card-front" aria-label="Business card front">
    <div class="front-band"></div>
    <div class="emblem" role="img" aria-label="Faint round regional emblem"></div>
    <div class="brand"><span class="brand-mark"></span>Verlane Area Planning Council</div>
    <div class="contact-rule"></div>
    <div class="contact">
      <p class="contact-name">Marlo Quint - CEO</p>
      <p class="contact-address">417 Merriwell Avenue, Harlow Falls,<br>ST 70000</p>
      <ul class="contact-list">
        <li><svg class="contact-icon" viewBox="0 0 12 12"><circle cx="6" cy="6" r="6" fill="var(--icon-blue)"/><path d="M4 3.2l1 1.2-.6.8c.4.9 1 1.5 1.9 1.9l.8-.6 1.2 1-.6 1.1C5.3 8.4 3.6 6.7 3.4 3.8z" fill="#fff"/></svg>5550192734</li>
        <li><svg class="contact-icon" viewBox="0 0 12 12"><circle cx="6" cy="6" r="6" fill="var(--icon-blue)"/><rect x="3.5" y="4" width="5" height="4" fill="none" stroke="#fff" stroke-width="0.9"/><rect x="4.5" y="2.8" width="3" height="1.4" fill="#fff"/></svg>5550192739</li>
        <li><svg class="contact-icon" viewBox="0 0 12 12"><circle cx="6" cy="6" r="6" fill="var(--icon-blue)"/><rect x="3.2" y="4" width="5.6" height="4" fill="none" stroke="#fff" stroke-width="0.8"/><path d="M3.2 4l2.8 2.2L8.8 4" fill="none" stroke="#fff" stroke-width="0.8"/></svg>dana@vlpk.example</li>
        <li><svg class="contact-icon" viewBox="0 0 12 12"><circle cx="6" cy="6" r="6" fill="var(--icon-blue)"/><circle cx="6" cy="6" r="2.8" fill="none" stroke="#fff" stroke-width="0.8"/><path d="M3.2 6h5.6M6 3.2v5.6" stroke="#fff" stroke-width="0.6"/></svg>www.vlpk.example</li>
      </ul>
    </div>
  </section>

  <section class="card card-back" aria-label="Business card back">
    <div class="emblem" role="img" aria-label="Faint round regional emblem"></div>
    <div class="brand"><span class="brand-mark"></span>Verlane Area Planning Council</div>
  </section>
</body>
</html>
```